Graphic background for 10 Pull Up Banners

To produce a graphic background for a 100 cm wide by 200 cm high Pull-Up Display banner containing a Buddhist text in three languages: Tibetan, Mandarin and English. Please refer to uploaded file "Elements of Pull Up Banner". The design should be simple (not drawing attention away from the text). This design should then be varied for or extended to the next banner and so on until the 10th banner. When the banners are lined up, they should form a single design that is 1000 cm wide by 200 cm high.
An alternative way to look at the project is to produce a graphic background of 1000 cm width by 200 cm height that is then splitted into ten separate 100 cm wide by 200 cm high graphic to be used as background for 10 Buddhist texts (text 1, 2, 3, 4, 5, 6, 7, 8, 9a, 9b) on 10 Pull-Up Display Banners, the text in each banner being in the three languages mentioned earlier.
In either perspective, the design should be simple and not draw attention away from the texts. See uploaded PDF file "Examples.pdf"
For attendees at a Buddhist Event.

```html
<!DOCTYPE html>
<html lang="en">
<head>
<meta charset="utf-8">
<title>Ten Mistaking – Pull-Up Banner</title>
<link href="https://fonts.googleapis.com/css2?family=Open+Sans:wght@400;600&family=Noto+Sans+SC:wght@400;500&family=Noto+Serif+Tibetan:wght@400&display=swap" rel="stylesheet">
<style>
  :root{
    --page:#ececec;
    --paper:#ffffff;
    --ink:#2b2b2b;
    --leaf-light:#9cc25a;
    --leaf-mid:#6e9e3a;
    --leaf-deep:#3f6e24;
    --band:#2f4f25;
    --band-text:#eef3e8;
    --panel:rgba(255,255,255,0.22);
    --brand:#b0323c;
  }
  *{margin:0;padding:0;box-sizing:border-box}
  html,body{width:1192px;height:1200px;overflow:hidden;background:var(--page)}
  .banner{position:absolute;left:358px;top:20px;width:475px;height:1160px;background:var(--paper);overflow:hidden;box-shadow:0 2px 10px rgba(0,0,0,.12)}
  .foliage{position:absolute;left:0;top:240px;width:100%;height:780px;
    background:
      radial-gradient(ellipse 60% 30% at 30% 55%, rgba(60,100,35,.55), transparent 70%),
      radial-gradient(ellipse 50% 25% at 75% 30%, rgba(80,120,45,.45), transparent 70%),
      linear-gradient(180deg, rgba(255,255,255,1) 0%, rgba(190,215,150,.9) 6%, var(--leaf-mid) 16%, var(--leaf-deep) 40%, var(--leaf-mid) 62%, var(--leaf-light) 85%, var(--leaf-mid) 100%);}
  .brand{position:absolute;left:48px;top:92px;display:flex;flex-direction:column;align-items:center;gap:6px;width:76px}
  .brand-dot{width:34px;height:34px;border-radius:50%;background:var(--brand)}
  .brand-name{font-family:"Open Sans",sans-serif;font-size:11px;font-weight:600;color:var(--brand);text-align:center;line-height:1.2}
  .title{position:absolute;left:172px;top:52px;color:var(--ink)}
  .title-zh{font-family:"Noto Sans SC",sans-serif;font-size:40px;font-weight:500;letter-spacing:2px;line-height:1.1}
  .title-en{font-family:"Open Sans",sans-serif;font-size:34px;font-weight:400;line-height:1.3}
  .panel{position:absolute;left:46px;top:262px;width:390px;height:738px;background:var(--panel);border-radius:10px}
  .verse-bo{position:absolute;left:125px;top:268px;font-family:"Noto Serif Tibetan",serif;font-size:11px;line-height:29px;color:var(--ink);list-style:none}
  .verse-zh{position:absolute;left:165px;top:566px;font-family:"Noto Sans SC",sans-serif;font-size:12.5px;line-height:16.5px;color:var(--ink);list-style:none}
  .notes{position:absolute;left:165px;top:740px;font-family:"Noto Sans SC",sans-serif;font-size:11.5px;line-height:17px;color:var(--ink);list-style:none}
  .verse-en{position:absolute;left:59px;top:788px;font-family:"Open Sans",sans-serif;font-size:7.5px;line-height:19.5px;color:var(--ink);list-style:none}
  .dedication{position:absolute;left:0;top:1010px;width:100%;height:150px;background:var(--band);color:var(--band-text)}
  .dedication-text{position:absolute;left:95px;top:28px;width:250px;text-align:center}
  .ded-bo{font-family:"Noto Serif Tibetan",serif;font-size:12px;line-height:22px}
  .ded-zh{font-family:"Noto Sans SC",sans-serif;font-size:11px;line-height:26px}
  .ded-en{font-family:"Open Sans",sans-serif;font-size:10px;line-height:26px}
  .lotus{position:absolute;left:356px;top:38px;width:54px;height:46px;border-radius:8px;background:rgba(255,255,255,.12)}
</style>
</head>
<body>
<main class="banner">
  <div class="foliage" role="img" aria-label="Softly blurred photograph of green garden foliage"></div>

  <div class="brand">
    <span class="brand-dot"></span>
    <span class="brand-name">Lotus Dharma Centre</span>
  </div>

  <header class="title">
    <h1 class="title-zh">十个误解</h1>
    <p class="title-en">Ten Mistaking</p>
  </header>

  <div class="panel"></div>

  <ul class="verse-bo" lang="bo">
    <li>དད་པ་དང་འདོད་པ་ལ་ནོར་སྲིད།</li>
    <li>བྱམས་སྙིང་རྗེ་དང་ཆགས་པ་ལ་ནོར་སྲིད།</li>
    <li>ཤེས་བྱའི་སྟོང་པ་དང་བློས་བྱས་སྟོང་ཉིད་ལ་ནོར་སྲིད།</li>
    <li>ཆོས་དབྱིངས་དང་ཆད་ལྟ་ལ་ནོར་སྲིད།</li>
    <li>ཉམས་མྱོང་དང་རྟོགས་པ་ལ་ནོར་སྲིད།</li>
    <li>ཆོས་པ་དང་ལྷ་པ་ལ་ནོར་སྲིད།</li>
    <li>འཁྲུལ་ཞིག་དང་གདོན་ཞུགས་ལ་ནོར་སྲིད།</li>
    <li>གྲུབ་ཐོབ་དང་གཡོ་ཅན་ལ་ནོར་སྲིད།</li>
    <li>གཞན་དོན་དང་རང་དོན་ལ་ནོར་སྲིད།</li>
    <li>ཐབས་མཁས་དང་གཡོ་སྒྱུ་ལ་ནོར་སྲིད།</li>
  </ul>

  <ul class="verse-zh" lang="zh">
    <li>信心与贪欲可能混淆，</li>
    <li>慈悲与执着可能混淆，</li>
    <li>所知1本空与思维造作空性可能混淆，</li>
    <li>法界与断见2可能混淆，</li>
    <li>觉受与证悟可能混淆，</li>
    <li>尊者与神棍可能混淆，</li>
    <li>破惑与着魔可能混淆，</li>
    <li>成就者与骗子可能混淆，</li>
    <li>利他与自利可能混淆，</li>
    <li>方便善巧与欺瞒诡诈可能混淆。</li>
  </ul>

  <ol class="notes" lang="zh">
    <li>1.&nbsp;&nbsp;所知：可以认知的外境。</li>
    <li>2.&nbsp;&nbsp;断见：否定因果、前生、后世等说法的见解。</li>
  </ol>

  <ul class="verse-en">
    <li>Desire can be mistaken for faith or devotion.</li>
    <li>Attachment can be mistaken for love and compassion.</li>
    <li>Conceptual emptiness can be mistaken for the emptiness of the nature of phenomena.</li>
    <li>Nihilism can be mistaken for the dharmadhatu.</li>
    <li>A meditative experience can be mistaken for realization.</li>
    <li>Outer religious practices can be mistaken for inner development of good qualities.</li>
    <li>A person in the grip of a demon can be mistaken for a person who has destroyed his own delusions.</li>
    <li>A charlatan can be mistaken for a siddha.</li>
    <li>An act to benefit yourself can be mistaken for an act to benefit others.</li>
    <li>Deviousness can be mistaken for skilful means.</li>
  </ul>

  <footer class="dedication">
    <div class="dedication-text">
      <p class="ded-bo" lang="bo">འགྲོ་བ་ཀུན་གྱིས་སངས་རྒྱས་ཐོབ་པར་ཤོག</p>
      <p class="ded-zh" lang="zh">愿诸有情共证佛果位。</p>
      <p class="ded-en">May all attain Buddhahood together.</p>
    </div>
    <div class="lotus" role="img" aria-label="White outline lotus flower icon"></div>
  </footer>
</main>
</body>
</html>
```